Sophrologist needs a cool signage at door entrance

I need signage for dr in sophrology based in Belgium (french speaking). The signed should capture the name the "Mireille Vantoorn" - "Naturopathe-Sophrologue-Reiki" and a catchphrase = (Healthy way of life)
« Fais du bien à ton corps, pour que ton âme ait envie d’y rester »
Requirements
Must have
- Hey,
Thats the instagram account for some inspiration www.instagram.com/mireille_serene_wellbeing
Light colors, green, blue
Healthy way of life
Size is 45cm wide on 30 cm high
The signage will be placed in front off woof pannel

```html
<!DOCTYPE html>
<html lang="fr">
<head>
<meta charset="utf-8">
<title>Mireille Vantoorn – Naturopathe-Sophrologue-Reiki</title>
<link href="https://fonts.googleapis.com/css2?family=Marcellus&family=Dancing+Script:wght@500&display=swap" rel="stylesheet">
<style>
  :root {
    --stage: #6e6e6e;
    --leaf-deep: #2f6d12;
    --leaf-mid: #5c9e22;
    --glow-light: #f6fbe0;
    --glow-lime: #c9e46a;
    --ink-blue: #0a3f93;
    --ink-green: #1f3a0a;
    --band-green: #4a6a0e;
    --frame-white: #ffffff;
  }
  * { margin: 0; padding: 0; box-sizing: border-box; }
  html, body {
    width: 1200px;
    height: 825px;
    overflow: hidden;
    background: var(--stage);
  }
  .sign {
    position: absolute;
    left: 0;
    top: 12.5px;
    width: 1200px;
    height: 800px;
    overflow: hidden;
  }
  .sign__backdrop {
    position: absolute;
    inset: 0;
    background:
      radial-gradient(ellipse 45% 40% at 50% 38%, var(--glow-light) 0%, rgba(246,251,224,0.7) 35%, rgba(201,228,106,0) 75%),
      radial-gradient(ellipse 70% 60% at 50% 50%, var(--glow-lime) 0%, var(--leaf-mid) 70%, var(--leaf-deep) 100%);
  }
  .sign__foliage {
    position: absolute;
    left: 0;
    top: 0;
    width: 100%;
    height: 260px;
    background: linear-gradient(180deg, var(--leaf-deep) 0%, rgba(62,128,24,0.85) 45%, rgba(92,158,34,0) 100%);
  }
  .sign__frame {
    position: absolute;
    left: 28px;
    top: 30px;
    width: 1144px;
    height: 739px;
    border: 4px solid var(--frame-white);
  }
  .sign__name {
    position: absolute;
    left: 0;
    width: 100%;
    top: 228px;
    text-align: center;
    font-family: "Marcellus", serif;
    font-size: 80px;
    line-height: 1;
    letter-spacing: 2px;
    color: var(--ink-blue);
    -webkit-text-stroke: 2.2px var(--ink-blue);
    text-transform: uppercase;
  }
  .sign__rule {
    position: absolute;
    left: 123px;
    width: 953px;
    top: 325px;
    height: 1px;
    background: var(--ink-green);
  }
  .sign__role {
    position: absolute;
    left: 0;
    width: 100%;
    top: 344px;
    text-align: center;
    font-family: "Marcellus", serif;
    font-size: 46px;
    line-height: 1;
    color: var(--ink-green);
  }
  .sign__motto {
    position: absolute;
    left: 0;
    width: 100%;
    top: 400px;
    text-align: center;
    font-family: "Dancing Script", cursive;
    font-weight: 500;
    font-size: 150px;
    line-height: 1.1;
    color: var(--ink-blue);
    white-space: nowrap;
  }
  .sign__quote-band {
    position: absolute;
    left: 106px;
    top: 665px;
    width: 989px;
    height: 60px;
    background: var(--band-green);
    display: flex;
    align-items: center;
    justify-content: center;
  }
  .sign__quote {
    font-family: "Marcellus", serif;
    font-size: 29px;
    color: var(--frame-white);
    white-space: nowrap;
  }
</style>
</head>
<body>
  <main class="sign">
    <div class="sign__backdrop" role="img" aria-label="Soft blurred green and yellow foliage with light bokeh"></div>
    <div class="sign__foliage" role="img" aria-label="Hanging green leaves along the top edge"></div>
    <div class="sign__frame"></div>
    <h1 class="sign__name">Mireille Vantoorn</h1>
    <div class="sign__rule"></div>
    <p class="sign__role">Naturopathe-Sophrologue-Reiki</p>
    <p class="sign__motto">Healthy way of life</p>
    <div class="sign__quote-band">
      <p class="sign__quote">Fais du bien à ton corps, pour que ton âme ait envie d’y rester</p>
    </div>
  </main>
</body>
</html>
```